Business card for Medication Therapy Management company
Corvale MTM
Professional
Lionel Fairbrook
PharmD
4873 Wexley St.
Denver, CO
lionel@corvalemtm.com
www.corvalemtm.com
logo attached.... please also see elements of website at www.corvalemtm.com

```html
<!DOCTYPE html>
<html lang="en">
<head>
<meta charset="utf-8">
<title>Corvale MTM Stationery</title>
<link href="https://fonts.googleapis.com/css2?family=Montserrat:wght@400;600&display=swap" rel="stylesheet">
<style>
  :root{
    --bg:#3a3a3c;
    --paper:#ffffff;
    --ink:#4a4a4d;
    --muted:#8a8a8e;
    --accent:#d9322b;
    --navy:#2f3842;
    --navy-dark:#1f262e;
  }
  *{margin:0;padding:0;box-sizing:border-box}
  html,body{width:1200px;height:461px;overflow:hidden}
  body{background:var(--bg);font-family:"Montserrat",Arial,sans-serif;color:var(--ink);position:relative}
  .sheet{position:absolute;background:var(--paper);box-shadow:0 4px 10px rgba(0,0,0,.35)}
  .logo{display:flex;align-items:center;gap:3px;font-weight:600;letter-spacing:.5px;color:var(--ink);text-transform:uppercase;line-height:1}
  .logo .dot{border-radius:50%;background:var(--accent);display:inline-block}
  .tagline{font-size:3px;letter-spacing:.6px;text-transform:uppercase;color:var(--muted);margin-top:2px}

  .card-front{left:24px;top:156px;width:56px;height:56px;padding:8px 5px}
  .card-front .logo{font-size:6px}
  .card-front .logo .dot{width:5px;height:5px}
  .card-front .person{margin-top:9px;font-size:2.6px;line-height:1.5}
  .card-front .person b{color:var(--accent);font-weight:600}
  .card-back{left:24px;top:221px;width:56px;height:43px;background:linear-gradient(160deg,var(--navy),var(--navy-dark));padding:7px 5px}
  .card-back .logo{font-size:5px;color:#e6e6e6}
  .card-back .logo .dot{width:4px;height:4px}
  .card-back .line{margin-top:6px;height:1px;width:26px;background:var(--accent)}

  .letterhead{top:41px;width:271px;height:386px;padding:22px 20px}
  .lh-one{left:192px}
  .lh-two{left:504px}
  .letterhead .logo{font-size:11px}
  .letterhead .logo .dot{width:9px;height:9px}
  .contact{position:absolute;right:26px;top:20px;font-size:3.2px;line-height:1.8;color:var(--muted)}
  .contact .row{display:flex;align-items:center;gap:3px}
  .contact .row::before{content:"";width:3px;height:3px;border-radius:50%;background:var(--accent)}
  .contact .name{color:var(--ink);font-weight:600}

  .env-back{left:814px;top:41px;width:360px;height:146px;overflow:hidden}
  .env-back svg{position:absolute;left:0;top:0}
  .env-back .logo{position:absolute;left:50%;top:27px;transform:translateX(-50%);font-size:8px;color:#e6e6e6}
  .env-back .logo .dot{width:7px;height:7px}
  .env-back .return{position:absolute;left:0;right:0;top:42px;text-align:center;font-size:3.4px;color:#b8bcc2;letter-spacing:.4px}

  .env-front{left:814px;top:250px;width:360px;height:177px;padding:28px 30px}
  .env-front .logo{font-size:11px}
  .env-front .logo .dot{width:9px;height:9px}
  .recipient{position:absolute;left:150px;top:118px;font-size:4px;line-height:1.7;color:var(--muted);letter-spacing:.3px}
</style>
</head>
<body>

<div class="sheet card-front">
  <div class="logo">Corvale MTM <span class="dot"></span></div>
  <div class="tagline">Medication Therapy Management</div>
  <div class="person">
    <b>Lionel Fairbrook</b>, PharmD<br>
    4873 Wexley St. Denver, CO<br>
    lionel@corvalemtm.com<br>
    www.corvalemtm.com
  </div>
</div>

<div class="sheet card-back">
  <div class="logo">Corvale MTM <span class="dot"></span></div>
  <div class="line"></div>
</div>

<div class="sheet letterhead lh-one">
  <div class="logo">Corvale MTM <span class="dot"></span></div>
  <div class="tagline">Medication Therapy Management</div>
  <div class="contact">
    <div class="name">Lionel Fairbrook</div>
    <div class="row">4873 Wexley St.</div>
    <div class="row">Denver, CO</div>
    <div class="row">lionel@corvalemtm.com</div>
    <div class="row">www.corvalemtm.com</div>
  </div>
</div>

<div class="sheet letterhead lh-two">
  <div class="contact" style="left:20px;right:auto">
    <div class="name">Lionel Fairbrook</div>
    <div class="row">4873 Wexley St.</div>
    <div class="row">Denver, CO</div>
    <div class="row">lionel@corvalemtm.com</div>
  </div>
  <div style="position:absolute;right:20px;top:22px" class="logo-wrap">
    <div class="logo" style="font-size:11px">Corvale MTM <span class="dot" style="width:9px;height:9px"></span></div>
  </div>
</div>

<div class="sheet env-back">
  <svg width="360" height="146" viewBox="0 0 360 146" aria-hidden="true">
    <defs>
      <linearGradient id="flap" x1="0" y1="0" x2="0" y2="1">
        <stop offset="0" stop-color="#3b4550"/>
        <stop offset="1" stop-color="#1f262e"/>
      </linearGradient>
    </defs>
    <polygon points="0,0 360,0 360,8 180,62 0,8" fill="url(#flap)"/>
    <polyline points="0,146 150,70 210,70 360,146" fill="none" stroke="#e4e4e6" stroke-width="1"/>
  </svg>
  <div class="logo">Corvale MTM <span class="dot"></span></div>
  <div class="return">4873 Wexley St. Denver, CO</div>
</div>

<div class="sheet env-front">
  <div class="logo">Corvale MTM <span class="dot"></span></div>
  <div class="tagline">Medication Therapy Management</div>
  <div class="recipient">Recipient Name<br>Street Address, City</div>
</div>

</body>
</html>
```